Quiet Ledger needs a book cover

Enabling people to find a new way of looking at money. If peoples thoughts, attitude and emotions around money are not inline with their goals and dreams then it is often harder to achieve their version of success.

Recognition that we have an emotional and a practical way with money.

Quiet Ledger enables people to find a sustainable (balanced) way with money for their life right now and their future.

Developing this over the years and seeing clients achieve a clear picture/idea/thought connection that is positive around money and it's purpose to them in their lives has truly been fabulous as they have then gone on to achieve their goals and dreams.

Title of book = Quiet Ledger
Tag line = Being healthy being wealthy
Authors Name = Ruth Pell
Book Size = 135 width x 185 height
Thumbnail = Cover must work well as well as full size
Looking for simple and clear app-able / icon type image
Feel free to have fun with it
A simple yet refreshing balanced, eye-catching design.

The back will include authors photo, blurb, testimonials, barcode, ISBN number & price. I will provide once front cover is sorted.

Reason: Realised that the tag line for the book was incorrect.

Target Market(s)

Individuals

Industry/Entity Type

Work

Requirements
Must have
• First work on front cover, once approved we can then do spine and back cover

```html
<!DOCTYPE html>
<html lang="en">
<head>
<meta charset="utf-8">
<title>Quiet Ledger – Book Cover</title>
<link href="https://fonts.googleapis.com/css2?family=Libre+Baskerville:wght@700&family=Tinos:wght@400;700&display=swap" rel="stylesheet">
<style>
  :root {
    --page-bg: #eeeeec;
    --cover-bg: #e9e7be;
    --title-green: #1d6a33;
    --title-shadow: #b9c79a;
    --body-ink: #2a2a22;
    --placeholder-box: #8d8c82;
    --placeholder-ink: #2b2b26;
    --photo-top: #f1efe4;
    --photo-mid: #d9b66a;
    --photo-low: #b98a3c;
    --photo-base: #8f5e2c;
  }
  * { margin: 0; padding: 0; box-sizing: border-box; }
  html, body { width: 1200px; height: 800px; overflow: hidden; background: var(--page-bg); }
  .jacket {
    position: absolute; left: 113px; top: 80px;
    display: flex; height: 640px;
  }
  .cover {
    position: relative; width: 467px; height: 640px;
    background: var(--cover-bg); overflow: hidden;
  }
  .spine {
    position: relative; width: 40px; height: 640px;
    background: var(--cover-bg);
    border-left: 1px solid rgba(0,0,0,.08);
    border-right: 1px solid rgba(0,0,0,.08);
  }
  .author-credit {
    position: absolute; right: 34px; top: 28px;
    font-family: "Libre Baskerville", serif; font-weight: 700;
    font-size: 17px; color: var(--body-ink); letter-spacing: .3px;
  }
  .book-title {
    position: absolute; left: 0; right: 0; top: 52px;
    font-family: "Libre Baskerville", serif; font-weight: 700;
    font-size: 78px; line-height: 0.98; letter-spacing: -2px;
    text-align: center; color: var(--title-green);
    text-shadow: 3px 3px 0 var(--title-shadow);
  }
  .tagline {
    position: absolute; left: 0; right: 0; top: 240px;
    font-family: "Libre Baskerville", serif; font-weight: 700;
    font-size: 14px; text-align: center; color: var(--title-green);
    letter-spacing: .2px;
  }
  .cover-photo {
    position: absolute; left: 0; right: 0; top: 300px; bottom: 0;
    background: linear-gradient(180deg, var(--photo-top) 0%, var(--photo-top) 30%, var(--photo-mid) 52%, var(--photo-low) 78%, var(--photo-base) 100%);
  }
  /* back cover */
  .back .author-credit { font-size: 14px; top: 24px; }
  .back .book-title { font-size: 66px; top: 44px; }
  .back .tagline { top: 208px; font-size: 12px; }
  .blurb {
    position: absolute; left: 30px; right: 30px; top: 238px;
    font-family: "Tinos", serif; font-weight: 700; font-size: 11.2px;
    line-height: 1.28; text-align: justify; color: var(--body-ink);
  }
  .placeholder {
    position: absolute; top: 560px; width: 126px; height: 52px;
    background: var(--placeholder-box);
    display: flex; align-items: center; justify-content: center;
    font-family: "Tinos", serif; font-size: 11px; color: var(--placeholder-ink);
  }
  .placeholder.logo { left: 46px; }
  .placeholder.isbn { right: 46px; }
  /* spine */
  .spine-title {
    position: absolute; left: 50%; top: 18px;
    writing-mode: vertical-rl;
    transform: translateX(-50%);
    font-family: "Libre Baskerville", serif; font-weight: 700;
    font-size: 30px; letter-spacing: -1px; color: var(--title-green);
    text-shadow: 1px 1px 0 var(--title-shadow);
  }
  .spine-author {
    position: absolute; left: 50%; bottom: 22px;
    writing-mode: vertical-rl; transform: translateX(-50%);
    font-family: "Libre Baskerville", serif; font-weight: 700;
    font-size: 10px; color: var(--body-ink); letter-spacing: .5px;
  }
</style>
</head>
<body>
  <div class="jacket">
    <section class="cover back">
      <p class="author-credit">RUTH PELL’S</p>
      <h2 class="book-title">QUIET<br>LEDGER</h2>
      <p class="tagline">WHAT IS THE PURPOSE OF MONEY IN YOUR LIFE?</p>
      <p class="blurb">Lorem ipsum dolor sit amet, consectetur adipisicing elit, sed do eiusmod tempor incididunt ut labore et dolore magna aliqua. Ut enim ad minim veniam, quis nostrud exercitation. Lorem ipsum dolor sit amet, consectetur adipisicing elit, sed do eiusmod tempor incididunt ut labore et dolore magna aliqua. Ut enim ad minim veniam, quis nostrud exercitation. Lorem ipsum dolor sit amet, consectetur adipisicing elit, sed do eiusmod tempor incididunt ut labore et dolore magna aliqua. Ut enim ad minim veniam, quis nostrud exercitation. Lorem ipsum dolor sit amet, consectetur adipisicing elit, sed do eiusmod tempor incididunt ut labore et dolore magna aliqua. Ut enim ad minim veniam, quis nostrud exercitation. Lorem ipsum dolor sit amet, consectetur adipisicing elit, sed do eiusmod tempor incididunt ut labore et dolore magna aliqua. Ut enim ad minim veniam, quis nostrud exercitation. Lorem ipsum dolor sit amet, consectetur adipisicing elit, sed do eiusmod tempor incididunt ut labore et dolore magna aliqua. Ut enim ad minim veniam, quis nostrud exercitation. Lorem ipsum dolor sit amet, consectetur adipisicing elit, sed do eiusmod tempor incididunt ut labore et dolore magna aliqua. Ut enim ad minim veniam, quis nostrud exercitation. Lorem ipsum dolor sit amet, consectetur adipisicing elit, sed do eiusmod tempor incididunt ut labore et dolore magna aliqua. Ut enim ad minim veniam, quis nostrud exercitation.</p>
      <div class="placeholder logo">LOGO</div>
      <div class="placeholder isbn">ISBN</div>
    </section>

    <section class="spine">
      <p class="spine-title">QUIET LEDGER</p>
      <p class="spine-author">RUTH PELL</p>
    </section>

    <section class="cover front">
      <p class="author-credit">RUTH PELL’S</p>
      <h1 class="book-title">QUIET<br>LEDGER</h1>
      <p class="tagline">WHAT IS THE PURPOSE OF MONEY IN YOUR LIFE?</p>
      <div class="cover-photo" role="img" aria-label="Photo of business people standing and balancing on stacks of gold and copper coins over a field of scattered coins"></div>
    </section>
  </div>
</body>
</html>
```